Football blog needs a Wordpress design new site

We need a wordpress design for a new football blog site. We would like to see a design that uses the colours green, white and black and one that makes good use of the slideshow widgets as scene in the site 'www.trenvix.net'
We would like a modern and sleek looking site but one that is also professional and easy to navigate.
Unfortunately due to unforeseen circumstances we are having to shorten the deadline date for this project.
The new deadline date is 16/07/2014.
We apologise for any inconveniance
It Professional

```html
<!DOCTYPE html>
<html lang="en">
<head>
<meta charset="utf-8">
<title>Pitchside Natter — Football Blog</title>
<link rel="stylesheet" href="https://fonts.googleapis.com/css2?family=Oswald:wght@400;500;600&family=Open+Sans:wght@400;600;700&display=swap">
<style>
:root{
  --green:#27a844;
  --green-dark:#1d8a36;
  --black:#111214;
  --ink:#1c1c1c;
  --grey:#8a8a8a;
  --line:#e2e2e2;
  --paper:#ffffff;
  --topbar:#efefef;
  --footer:#161616;
  --footer-base:#0c0c0c;
  --blue:#3b5a9a;
  --sky:#2aa3dc;
  --red:#d8432f;
  --pink:#e23d75;
  --orange:#f08a24;
}
*{box-sizing:border-box;margin:0;padding:0}
html,body{width:1200px;height:3279px;overflow:hidden;background:var(--paper)}
body{font-family:"Open Sans",Arial,sans-serif;color:var(--ink);font-size:11px;position:relative}
.h{font-family:"Oswald","Arial Narrow",sans-serif;text-transform:uppercase}
.abs{position:absolute}
.wrap{position:absolute;left:155px;width:890px}

/* photo placeholders */
.ph{display:block;position:relative;overflow:hidden}
.ph-pitch{background:linear-gradient(135deg,#1f3b2a 0%,#3f7d3d 45%,#2a5a8a 100%)}
.ph-night{background:linear-gradient(160deg,#0e1a26 0%,#24465e 55%,#3f7a3b 100%)}
.ph-crowd{background:linear-gradient(135deg,#6b2418 0%,#c0532c 45%,#e2b13c 100%)}
.ph-grass{background:linear-gradient(180deg,#2f6f33 0%,#54a447 100%)}
.ph-red{background:linear-gradient(135deg,#3a0f12 0%,#a3262b 55%,#d9d2cc 100%)}

/* top bar */
.topbar{left:0;top:0;width:1200px;height:33px;background:var(--topbar)}
.topbar .links{position:absolute;left:155px;top:9px;display:flex;gap:16px;font-size:10px;color:#555}
.topbar .follow{position:absolute;right:155px;top:9px;display:flex;gap:5px;align-items:center;font-size:10px;color:#555}
.sq{display:inline-block;width:13px;height:13px;border-radius:2px}
.logo{left:155px;top:42px;display:flex;align-items:center;gap:10px}
.logo .dot{width:48px;height:48px;border-radius:50%;background:var(--green)}
.logo span{font-family:"Oswald",sans-serif;font-size:20px;font-weight:500;color:var(--black)}

/* nav */
.nav{left:0;top:125px;width:1200px;height:40px;background:var(--black)}
.nav ul{position:absolute;left:155px;top:0;display:flex;list-style:none;height:40px}
.nav li{font-family:"Oswald",sans-serif;text-transform:uppercase;color:#fff;font-size:13px;padding:0 16px;line-height:40px}
.nav li.on{background:var(--green)}
.nav .search{position:absolute;right:165px;top:12px}

/* slider */
.slider{top:184px;height:334px;background:var(--black)}
.slider .main{position:absolute;left:0;top:0;width:590px;height:334px}
.cap{position:absolute;left:0;right:0;bottom:0;padding:14px 18px;background:linear-gradient(0deg,rgba(0,0,0,.85),rgba(0,0,0,0))}
.cap .tag{display:inline-block;background:var(--green);color:#fff;font-size:9px;padding:2px 6px;margin-bottom:6px}
.cap .t{color:#fff;font-size:19px;font-family:"Oswald",sans-serif;text-transform:uppercase;line-height:1.2}
.cap .d{color:#bbb;font-size:9px;margin-top:4px}
.slider .list{position:absolute;left:598px;top:0;width:292px}
.slider .item{display:flex;gap:10px;height:83.5px;padding:10px 8px;border-bottom:1px solid #2a2a2a}
.slider .item .ph{width:82px;height:62px;flex:none}
.slider .item .t{color:#fff;font-family:"Oswald",sans-serif;font-size:12.5px;text-transform:uppercase;line-height:1.3}
.slider .item .d{color:#888;font-size:9px;margin-top:5px}

/* section header */
.sh{height:30px;border-bottom:2px solid var(--line);position:relative}
.sh h2{font-family:"Oswald",sans-serif;font-size:19px;font-weight:500;text-transform:uppercase;color:var(--black);line-height:28px;display:inline-block;border-bottom:3px solid var(--green);padding-bottom:1px}
.tabs{position:absolute;right:0;top:9px;display:flex;gap:0;font-size:9px;text-transform:uppercase}
.tabs span{padding:0 8px;border-left:1px solid var(--line);color:#777}
.tabs span:first-child{border:0;color:var(--green);font-weight:700}

.card .t{font-family:"Oswald",sans-serif;text-transform:uppercase;font-size:12.5px;margin-top:8px;color:var(--black)}
.meta{font-size:9px;color:var(--grey);margin-top:4px;display:flex;gap:14px}
.ex{font-size:10px;color:#666;line-height:1.5;margin-top:5px}

/* main column + sidebar */
.maincol{left:155px;width:632px}
.side{left:830px;width:215px}

.tn-list .row{padding:0 0 12px 0;margin-bottom:12px;border-bottom:1px solid var(--line)}
.tn-list .t{font-family:"Oswald",sans-serif;text-transform:uppercase;font-size:12.5px;line-height:1.35;padding-left:12px;position:relative}
.tn-list .t:before{content:"";position:absolute;left:0;top:6px;width:5px;height:5px;background:var(--green)}
.btn{display:inline-block;background:var(--green);color:#fff;font-family:"Oswald",sans-serif;text-transform:uppercase;font-size:11px;padding:6px 14px}

.social{display:grid;grid-template-columns:repeat(4,1fr);gap:4px}
.social div{height:78px;color:#fff;text-align:center;padding-top:38px;font-size:10px;font-weight:700;line-height:1.2}
.social small{display:block;font-weight:400;font-size:8px}

.pp .row{display:flex;gap:10px;padding:10px 0;border-bottom:1px solid var(--line)}
.pp .ph{width:78px;height:58px;flex:none}
.pp .t{font-family:"Oswald",sans-serif;text-transform:uppercase;font-size:12px;color:var(--green);line-height:1.3}

.mp .box{height:172px;margin-bottom:10px}
.mp .cap .t{font-size:13px}

.play{position:absolute;left:50%;top:50%;transform:translate(-50%,-50%)}

.blog .post{display:flex;gap:18px;height:140px;margin-bottom:6px}
.blog .ph{width:220px;height:128px;flex:none}
.blog .t{font-family:"Oswald",sans-serif;text-transform:uppercase;font-size:14px;color:var(--black)}
.blog .d{font-size:9px;color:var(--green);margin-top:4px}
.shares{display:flex;gap:4px;margin-top:8px}

/* footer */
.footer{left:0;top:2899px;width:1200px;height:380px;background:var(--footer)}
.fcol{position:absolute;top:34px;color:#aaa}
.fcol h3{font-family:"Oswald",sans-serif;text-transform:uppercase;color:#fff;font-size:17px;font-weight:500;margin-bottom:14px;padding-bottom:6px;border-bottom:2px solid #2b2b2b}
.fsocial{display:grid;grid-template-columns:repeat(4,42px);gap:5px;margin-top:14px}
.fsocial div{height:42px}
.rev{display:flex;gap:10px;margin-bottom:12px}
.rev .ph{width:60px;height:46px;flex:none}
.rev .t{font-family:"Oswald",sans-serif;text-transform:uppercase;font-size:11px;color:#fff;line-height:1.3}
.rev .m{font-size:9px;color:var(--green);margin-top:4px}
.field{height:30px;background:#222;border:1px solid #2e2e2e;margin-top:10px;color:#777;font-size:10px;padding:8px}
.sub{height:32px;background:var(--green);color:#fff;text-align:center;font-family:"Oswald",sans-serif;text-transform:uppercase;font-size:13px;line-height:32px;margin-top:12px}
.fbase{position:absolute;left:0;bottom:0;width:1200px;height:40px;background:var(--footer-base);color:#888;font-size:10px}
.fbase .l{position:absolute;left:155px;top:14px}
.fbase .r{position:absolute;right:155px;top:14px;display:flex;gap:18px}
</style>
</head>
<body>

<header>
  <div class="abs topbar">
    <div class="links"><span>Home</span><span>About Us</span><span>Advertising</span><span>Contact Us</span></div>
    <div class="follow"><span>Follow:</span><i class="sq" style="background:var(--blue)"></i><i class="sq" style="background:var(--sky)"></i><i class="sq" style="background:var(--red)"></i><i class="sq" style="background:var(--orange)"></i></div>
  </div>
  <div class="abs logo"><i class="dot"></i><span>Pitchside Natter</span></div>
  <nav class="abs nav">
    <ul><li class="on">Home</li><li>Pitchside Blog</li><li>World Cup</li><li>Top News</li><li>Video</li><li>Competitions</li></ul>
    <svg class="search" width="16" height="16" viewBox="0 0 16 16"><circle cx="6.5" cy="6.5" r="5" fill="none" stroke="#fff" stroke-width="2"/><line x1="10.5" y1="10.5" x2="15" y2="15" stroke="#fff" stroke-width="2"/></svg>
  </nav>
</header>

<section class="wrap slider">
  <div class="main ph ph-pitch" role="img" aria-label="Players challenging for the ball on a floodlit pitch">
    <div class="cap"><span class="tag">Headlines</span><div class="t">Lorem ipsum is simply dummy text of the...</div><div class="d">July 14, 2014 · 0 Comments</div></div>
  </div>
  <div class="list">
    <div class="item"><i class="ph ph-night" role="img" aria-label="Striker on the ball"></i><div><div class="t">Lorem ipsum is simply dummy text of the...</div><div class="d">July 14, 2014</div></div></div>
    <div class="item"><i class="ph ph-pitch" role="img" aria-label="Midfield tackle"></i><div><div class="t">Lorem ipsum is simply dummy text of the...</div><div class="d">July 14, 2014</div></div></div>
    <div class="item"><i class="ph ph-grass" role="img" aria-label="Ball on the grass"></i><div><div class="t">Lorem ipsum is simply dummy text of the...</div><div class="d">July 14, 2014</div></div></div>
    <div class="item"><i class="ph ph-night" role="img" aria-label="Goalkeeper diving"></i><div><div class="t">Lorem ipsum is simply dummy text of the...</div><div class="d">July 14, 2014</div></div></div>
  </div>
</section>

<section class="wrap" style="top:535px">
  <div class="sh"><h2>Latest News</h2><div class="tabs"><span>Headlines</span><span>Recent Posts</span><span>Popular Posts</span></div></div>
  <div style="display:grid;grid-template-columns:repeat(4,1fr);gap:18px;margin-top:12px">
    <div class="card"><i class="ph ph-red" style="height:115px" role="img" aria-label="Players in red kits"></i><div class="t">Lorem ipsum is simply</div><div class="meta"><span>July 14, 2014</span></div></div>
    <div class="card"><i class="ph ph-pitch" style="height:115px" role="img" aria-label="Match action"></i><div class="t">Lorem ipsum is simply</div><div class="meta"><span>July 14, 2014</span></div></div>
    <div class="card"><i class="ph ph-crowd" style="height:115px" role="img" aria-label="Fans celebrating in the stand"></i><div class="t">Lorem ipsum is simply</div><div class="meta"><span>July 14, 2014</span></div></div>
    <div class="card"><i class="ph ph-night" style="height:115px" role="img" aria-label="Player shooting"></i><div class="t">Lorem ipsum is simply</div><div class="meta"><span>July 14, 2014</span></div></div>
  </div>
</section>

<main>
<section class="abs maincol" style="top:780px">
  <div class="sh"><h2>Pitchside News</h2><div class="tabs"><span>Headlines</span><span>Recent Posts</span><span>Popular Posts</span></div></div>
  <div style="display:flex;gap:16px;margin-top:14px">
    <div style="width:330px">
      <i class="ph ph-night" style="height:180px" role="img" aria-label="Player striking a ball"></i>
      <div class="card"><div class="t">Lorem ipsum is simply dummy text of the printing and typesetting</div><div class="meta"><span>July 14, 2014</span><span>0 Comments</span></div>
      <p class="ex">Fans flocked to the ground as the side kept up a strong run of form, with late goals settling a tense derby on a warm summer night.</p>
      <div style="margin-top:12px"><span class="btn">Read More</span></div></div>
    </div>
    <div class="tn-list" style="flex:1">
      <div class="row"><div class="t">Lorem ipsum is simply dummy text of the printing and typesetting</div><div class="meta"><span>July 14, 2014</span><span>0 Comments</span></div></div>
      <div class="row"><div class="t">Lorem ipsum is simply dummy text of the printing and typesetting</div><div class="meta"><span>July 14, 2014</span><span>0 Comments</span></div></div>
      <div class="row"><div class="t">Lorem ipsum is simply dolor of the printing and typesetting</div><div class="meta"><span>July 14, 2014</span><span>0 Comments</span></div></div>
      <div class="row"><div class="t">Lorem ipsum is simply dummy text of the printing and typesetting</div><div class="meta"><span>July 14, 2014</span><span>0 Comments</span></div></div>
    </div>
  </div>
</section>

<section class="abs maincol" style="top:1187px">
  <div class="sh"><h2>News in Pictures</h2><div class="tabs"><span>Headlines</span><span>Recent Posts</span><span>Popular Posts</span></div></div>
  <div style="display:flex;gap:4px;margin-top:14px;height:275px">
    <div class="ph ph-pitch" style="width:330px" role="img" aria-label="Two players contesting the ball">
      <div class="cap"><span class="tag">Headlines</span><div class="t" style="font-size:15px">Lorem ipsum is simply text of the...</div><div class="d">July 14, 2014</div></div>
    </div>
    <div style="flex:1;display:grid;grid-template-columns:repeat(3,1fr);grid-template-rows:repeat(3,1fr);gap:4px">
      <i class="ph ph-grass" role="img" aria-label="Aerial view of the pitch"></i><i class="ph ph-night" role="img" aria-label="Match action"></i><i class="ph ph-pitch" role="img" aria-label="Player dribbling"></i>
      <i class="ph ph-night" role="img" aria-label="Header in the box"></i><i class="ph ph-red" role="img" aria-label="Players in red"></i><i class="ph ph-grass" role="img" aria-label="Ball on grass"></i>
      <i class="ph ph-pitch" role="img" aria-label="Tackle"></i><i class="ph ph-night" role="img" aria-label="Goal celebration"></i><i class="ph ph-crowd" role="img" aria-label="Crowd in the stand"></i>
    </div>
  </div>
</section>

<section class="abs maincol" style="top:1564px">
  <div class="sh"><h2>Events</h2><div class="tabs"><span>Headlines</span><span>Recent Posts</span><span>Popular Posts</span></div></div>
  <div style="display:grid;grid-template-columns:repeat(4,1fr);gap:22px 16px;margin-top:14px">
    <div class="card"><i class="ph ph-red" style="height:72px" role="img" aria-label="Event photo"></i><div class="t">Lorem ipsum is simply</div><p class="ex">Season tickets go on sale next week at the ground.</p><div class="meta"><span>July 14, 2014</span></div></div>
    <div class="card"><i class="ph ph-pitch" style="height:72px" role="img" aria-label="Event photo"></i><div class="t">Lorem ipsum is simply</div><p class="ex">Open training day for young fans this Saturday.</p><div class="meta"><span>July 14, 2014</span></div></div>
    <div class="card"><i class="ph ph-crowd" style="height:72px" role="img" aria-label="Event photo"></i><div class="t">Lorem ipsum is simply</div><p class="ex">Supporters club meet and greet with the squad.</p><div class="meta"><span>July 14, 2014</span></div></div>
    <div class="card"><i class="ph ph-night" style="height:72px" role="img" aria-label="Event photo"></i><div class="t">Lorem ipsum is simply</div><p class="ex">Pre-season friendly kicks off under the lights.</p><div class="meta"><span>July 14, 2014</span></div></div>
    <div class="card"><i class="ph ph-pitch" style="height:72px" role="img" aria-label="Event photo"></i><div class="t">Lorem ipsum is simply</div><p class="ex">Charity match raises funds for local clubs.</p><div class="meta"><span>July 14, 2014</span></div></div>
    <div class="card"><i class="ph ph-red" style="height:72px" role="img" aria-label="Event photo"></i><div class="t">Lorem ipsum is simply</div><p class="ex">New kit launch night with the first team.</p><div class="meta"><span>July 14, 2014</span></div></div>
    <div class="card"><i class="ph ph-crowd" style="height:72px" role="img" aria-label="Event photo"></i><div class="t">Lorem ipsum is simply</div><p class="ex">Five-a-side tournament returns this summer.</p><div class="meta"><span>July 14, 2014</span></div></div>
    <div class="card"><i class="ph ph-night" style="height:72px" role="img" aria-label="Event photo"></i><div class="t">Lorem ipsum is simply</div><p class="ex">Stadium tour dates announced for August.</p><div class="meta"><span>July 14, 2014</span></div></div>
  </div>
</section>

<section class="abs maincol" style="top:2000px">
  <div class="sh"><h2>Top Videos</h2></div>
  <div style="display:flex;gap:4px;margin-top:10px;height:282px;background:var(--black);padding:4px">
    <div class="ph ph-pitch" style="flex:1" role="img" aria-label="Video still of a match">
      <svg class="play" width="50" height="50" viewBox="0 0 50 50"><circle cx="25" cy="25" r="23" fill="rgba(0,0,0,.5)" stroke="#fff" stroke-width="2"/><path d="M20 15 L35 25 L20 35Z" fill="#fff"/></svg>
    </div>
    <div style="width:200px;display:grid;grid-template-columns:1fr 1fr;grid-template-rows:repeat(3,1fr);gap:4px">
      <div class="ph ph-night" role="img" aria-label="Video thumbnail"><svg class="play" width="22" height="22" viewBox="0 0 22 22"><circle cx="11" cy="11" r="10" fill="rgba(0,0,0,.5)" stroke="#fff"/><path d="M9 6 L16 11 L9 16Z" fill="#fff"/></svg></div>
      <div class="ph ph-pitch" role="img" aria-label="Video thumbnail"><svg class="play" width="22" height="22" viewBox="0 0 22 22"><circle cx="11" cy="11" r="10" fill="rgba(0,0,0,.5)" stroke="#fff"/><path d="M9 6 L16 11 L9 16Z" fill="#fff"/></svg></div>
      <div class="ph ph-grass" role="img" aria-label="Video thumbnail"><svg class="play" width="22" height="22" viewBox="0 0 22 22"><circle cx="11" cy="11" r="10" fill="rgba(0,0,0,.5)" stroke="#fff"/><path d="M9 6 L16 11 L9 16Z" fill="#fff"/></svg></div>
      <div class="ph ph-night" role="img" aria-label="Video thumbnail"><svg class="play" width="22" height="22" viewBox="0 0 22 22"><circle cx="11" cy="11" r="10" fill="rgba(0,0,0,.5)" stroke="#fff"/><path d="M9 6 L16 11 L9 16Z" fill="#fff"/></svg></div>
      <div class="ph ph-red" role="img" aria-label="Video thumbnail"><svg class="play" width="22" height="22" viewBox="0 0 22 22"><circle cx="11" cy="11" r="10" fill="rgba(0,0,0,.5)" stroke="#fff"/><path d="M9 6 L16 11 L9 16Z" fill="#fff"/></svg></div>
      <div class="ph ph-pitch" role="img" aria-label="Video thumbnail"><svg class="play" width="22" height="22" viewBox="0 0 22 22"><circle cx="11" cy="11" r="10" fill="rgba(0,0,0,.5)" stroke="#fff"/><path d="M9 6 L16 11 L9 16Z" fill="#fff"/></svg></div>
    </div>
  </div>
</section>

<section class="abs maincol blog" style="top:2361px">
  <div class="sh"><h2>Our Blog</h2><div class="tabs"><span>Headlines</span><span>Recent Posts</span><span>Popular Posts</span></div></div>
  <div style="margin-top:14px">
    <article class="post"><i class="ph ph-night" role="img" aria-label="Player on the ball"></i><div><div class="t">Lorem ipsum dolor sit amet, consectetur adipiscing</div><div class="d">July 14, 2014</div><p class="ex">A strong second half turned the game around as the home side pressed high, won the ball back early and found space out wide to create chance after chance.</p><div class="shares"><i class="sq" style="background:var(--blue)"></i><i class="sq" style="background:var(--sky)"></i><i class="sq" style="background:var(--red)"></i><i class="sq" style="background:var(--orange)"></i></div></div></article>
    <article class="post"><i class="ph ph-red" role="img" aria-label="Players in red kits"></i><div><div class="t">Lorem ipsum dolor consectetur adipiscing dolor sit amet, consectetur</div><div class="d">July 14, 2014</div><p class="ex">The manager spoke after the match about new signings, the summer tour and his hopes for a young squad ready to push on this coming season.</p><div class="shares"><i class="sq" style="background:var(--blue)"></i><i class="sq" style="background:var(--sky)"></i><i class="sq" style="background:var(--red)"></i><i class="sq" style="background:var(--orange)"></i></div></div></article>
    <article class="post"><i class="ph ph-pitch" role="img" aria-label="Ball at a player's feet"></i><div><div class="t">Lorem ipsum dolor ipsum dolor sit amet, consectetur</div><div class="d">July 14, 2014</div><p class="ex">Our writers pick the best goals of the week, from long-range strikes to clever team moves finished with a cool touch in front of goal.</p><div class="shares"><i class="sq" style="background:var(--blue)"></i><i class="sq" style="background:var(--sky)"></i><i class="sq" style="background:var(--red)"></i><i class="sq" style="background:var(--orange)"></i></div></div></article>
  </div>
</section>
</main>

<aside>
<section class="abs side" style="top:830px">
  <div class="social">
    <div style="background:var(--blue)">12,540<small>Fans</small></div>
    <div style="background:var(--sky)">8,230<small>Followers</small></div>
    <div style="background:var(--red)">2,110<small>Followers</small></div>
    <div style="background:var(--pink)">1,480<small>Followers</small></div>
    <div style="background:var(--blue)">4,890<small>Likes</small></div>
    <div style="background:var(--red)">3,560<small>Subscribers</small></div>
    <div style="background:var(--pink)">920<small>Followers</small></div>
    <div style="background:var(--orange)">6,340<small>Readers</small></div>
  </div>
</section>

<section class="abs side pp" style="top:1059px">
  <div class="sh"><h2>Popular Posts</h2></div>
  <div class="ph ph-red" style="height:120px;margin-top:12px" role="img" aria-label="Players celebrating"><div class="cap" style="padding:8px 10px"><div class="t" style="font-size:12px">Lorem ipsum is simply...</div><div class="d">July 14, 2014</div></div></div>
  <div class="row"><i class="ph ph-night" role="img" aria-label="Post thumbnail"></i><div><div class="t">Lorem ipsum dummy text of the...</div><div class="meta"><span>July 14, 2014</span></div></div></div>
  <div class="row"><i class="ph ph-pitch" role="img" aria-label="Post thumbnail"></i><div><div class="t">Lorem ipsum dummy text of the...</div><div class="meta"><span>July 14, 2014</span></div></div></div>
  <div class="row"><i class="ph ph-red" role="img" aria-label="Post thumbnail"></i><div><div class="t">Lorem ipsum dummy text of the...</div><div class="meta"><span>July 14, 2014</span></div></div></div>
</section>

<section class="abs side mp" style="top:1525px">
  <div class="sh" style="margin-bottom:12px"><h2>Most Popular</h2></div>
  <div class="box ph ph-red" role="img" aria-label="Match action"><div class="cap"><span class="tag">Headlines</span><div class="t">Lorem ipsum is simply dummy...</div><div class="d">July 14, 2014</div></div></div>
  <div class="box ph ph-night" role="img" aria-label="Player in possession"><div class="cap"><span class="tag">Headlines</span><div class="t">Lorem ipsum is simply dummy...</div><div class="d">July 14, 2014</div></div></div>
  <div class="box ph ph-pitch" role="img" aria-label="Tackle on the wing"><div class="cap"><span class="tag">Headlines</span><div class="t">Lorem ipsum is simply dummy...</div><div class="d">July 14, 2014</div></div></div>
  <div class="box ph ph-night" role="img" aria-label="Shot on goal"><div class="cap"><span class="tag">Headlines</span><div class="t">Lorem ipsum is simply dummy...</div><div class="d">July 14, 2014</div></div></div>
  <div class="box ph ph-red" role="img" aria-label="Players in red kits"><div class="cap"><span class="tag">Headlines</span><div class="t">Lorem ipsum is simply dummy...</div><div class="d">July 14, 2014</div></div></div>
</section>
</aside>

<footer class="abs footer">
  <div class="fcol" style="left:155px;width:250px">
    <h3>Pitchside Natter</h3>
    <p class="ex" style="color:#999">Fresh football news, views and chat from the stands, every single day of the season.</p>
    <div class="fsocial">
      <div style="background:var(--blue)"></div><div style="background:var(--sky)"></div><div style="background:var(--red)"></div><div style="background:var(--pink)"></div>
      <div style="background:var(--red)"></div><div style="background:var(--blue)"></div><div style="background:var(--orange)"></div><div style="background:var(--pink)"></div>
    </div>
  </div>
  <div class="fcol" style="left:470px;width:250px">
    <h3>Best Reviews</h3>
    <div class="rev"><i class="ph ph-night" role="img" aria-label="Review thumbnail"></i><div><div class="t">Lorem ipsum is simply dummy text of the...</div><div class="m">July 14, 2014</div></div></div>
    <div class="rev"><i class="ph ph-pitch" role="img" aria-label="Review thumbnail"></i><div><div class="t">Lorem ipsum is simply dummy text of the...</div><div class="m">July 14, 2014</div></div></div>
    <div class="rev"><i class="ph ph-red" role="img" aria-label="Review thumbnail"></i><div><div class="t">Lorem ipsum is simply dummy text of the...</div><div class="m">July 14, 2014</div></div></div>
  </div>
  <div class="fcol" style="left:785px;width:260px">
    <h3>Weekly Newsletter</h3>
    <p class="ex" style="color:#999">Sign up for the weekly round-up of match reports, transfer talk and the best reads from our writers.</p>
    <div class="field">Your name</div>
    <div class="field">Your email</div>
    <div class="sub">Subscribe</div>
  </div>
  <div class="fbase">
    <span class="l">© Copyright 2014 Pitchside Natter</span>
    <span class="r"><span>Home</span><span>Pitchside Blog</span><span>World Cup</span><span>Top News</span><span>Media</span><span>Competitions</span></span>
  </div>
</footer>

</body>
</html>
```